occupational hygiene card design

We supply a service to the resource sector, commercial or government organisations to access health risks from physical or chemical hazards. We are a technical discipline that works within legislation.

Industry/Entity Type

Government

Contact Information for Business Card

KPLA
Kestrel plains occupational hygiene

```html
<!DOCTYPE html>
<html lang="en">
<head>
<meta charset="utf-8">
<title>KPLA business card</title>
<link rel="stylesheet" href="https://fonts.googleapis.com/css2?family=Exo+2:wght@400;600&display=swap">
<style>
  :root {
    --blue: #2e3192;
    --green-dark: #2f9a3a;
    --green-light: #7dcf2a;
    --green-text: #4caf32;
    --ink: #333333;
    --paper: #f7f7f7;
    --backdrop: #a3a3a3;
  }
  * { box-sizing: border-box; margin: 0; padding: 0; }
  html, body { width: 1200px; height: 895px; overflow: hidden; }
  body {
    background: var(--backdrop);
    font-family: "Exo 2", sans-serif;
    position: relative;
  }
  .card {
    position: absolute;
    left: 250px;
    width: 700px;
    height: 400px;
    background: var(--paper);
    overflow: hidden;
    box-shadow: 0 6px 18px rgba(0,0,0,.25);
  }
  .card--back { top: 26px; }
  .card--front { top: 468px; }

  .band { position: absolute; left: 0; width: 100%; display: block; }
  .band--top { top: 0; }
  .band--bottom { bottom: 0; }

  .brand { position: absolute; }
  .brand__name {
    font-weight: 600;
    color: var(--blue);
    line-height: 1;
    letter-spacing: 3px;
  }
  .brand__tagline {
    font-weight: 400;
    color: var(--ink);
    letter-spacing: 1px;
    margin-top: 8px;
    white-space: nowrap;
  }

  .card--back .brand { left: 0; width: 100%; top: 150px; text-align: center; }
  .card--back .brand__name { font-size: 48px; }
  .card--back .brand__tagline { font-size: 14px; }

  .card--front .brand { left: 70px; top: 68px; }
  .card--front .brand__name { font-size: 36px; }
  .card--front .brand__tagline { font-size: 11px; }

  .person { position: absolute; left: 470px; top: 92px; }
  .person__name {
    font-size: 24px;
    font-weight: 400;
    color: var(--green-text);
    letter-spacing: 2px;
  }
  .person__role {
    font-size: 10px;
    font-weight: 600;
    color: var(--ink);
    letter-spacing: 1px;
    margin-top: 6px;
  }

  .icon-strip { position: absolute; left: 0; top: 170px; width: 100%; display: block; }

  .contact {
    position: absolute;
    top: 262px;
    font-size: 15px;
    line-height: 1.45;
    color: var(--ink);
    letter-spacing: .5px;
  }
  .contact--web { left: 40px; }
  .contact--address { left: 270px; }
  .contact--phone { left: 500px; font-size: 17px; letter-spacing: 1.5px; }
</style>
</head>
<body>

<section class="card card--back" aria-label="Card back">
  <svg class="band band--top" width="700" height="60" viewBox="0 0 700 60" aria-hidden="true">
    <rect width="700" height="60" fill="var(--blue)"/>
    <polyline points="190,0 210,30 190,60" fill="none" stroke="#fff" stroke-width="6"/>
    <polyline points="540,0 560,30 540,60" fill="none" stroke="#fff" stroke-width="6"/>
  </svg>
  <div class="brand">
    <p class="brand__name">KPLA</p>
    <p class="brand__tagline">Kestrel plains occupational hygiene</p>
  </div>
  <svg class="band band--bottom" width="700" height="60" viewBox="0 0 700 60" aria-hidden="true">
    <rect width="700" height="60" fill="var(--blue)"/>
    <polyline points="160,0 180,30 160,60" fill="none" stroke="#fff" stroke-width="6"/>
    <polyline points="510,0 530,30 510,60" fill="none" stroke="#fff" stroke-width="6"/>
  </svg>
</section>

<section class="card card--front" aria-label="Card front">
  <svg class="band band--top" width="700" height="30" viewBox="0 0 700 30" aria-hidden="true">
    <rect width="700" height="30" fill="var(--blue)"/>
  </svg>

  <div class="brand">
    <p class="brand__name">KPLA</p>
    <p class="brand__tagline">Kestrel plains occupational hygiene</p>
  </div>

  <div class="person">
    <p class="person__name">MARA QUELL</p>
    <p class="person__role">GRAPHICS DESIGNER</p>
  </div>

  <svg class="icon-strip" width="700" height="60" viewBox="0 0 700 60" aria-hidden="true">
    <defs>
      <linearGradient id="strip-green" x1="0" x2="1" y1="0" y2="0">
        <stop offset="0" stop-color="var(--green-dark)"/>
        <stop offset=".5" stop-color="var(--green-light)"/>
        <stop offset="1" stop-color="var(--green-dark)"/>
      </linearGradient>
    </defs>
    <rect width="700" height="60" fill="url(#strip-green)"/>
    <polyline points="225,0 245,30 225,60" fill="none" stroke="#fff" stroke-width="7"/>
    <polyline points="455,0 475,30 455,60" fill="none" stroke="#fff" stroke-width="7"/>
    <g class="icon icon--globe" fill="none" stroke="#fff" stroke-width="2">
      <circle cx="110" cy="30" r="13"/>
      <ellipse cx="110" cy="30" rx="6" ry="13"/>
      <line x1="97" y1="30" x2="123" y2="30"/>
      <line x1="100" y1="22" x2="120" y2="22"/>
      <line x1="100" y1="38" x2="120" y2="38"/>
    </g>
    <g class="icon icon--pin" fill="#fff">
      <path d="M345 15 a10 10 0 0 1 10 10 c0 8 -10 20 -10 20 s-10 -12 -10 -20 a10 10 0 0 1 10 -10z"/>
      <circle cx="345" cy="25" r="4" fill="var(--green-light)"/>
    </g>
    <g class="icon icon--phone" fill="none" stroke="#fff" stroke-width="2">
      <rect x="572" y="14" width="18" height="32" rx="3"/>
      <line x1="578" y1="41" x2="584" y2="41"/>
    </g>
  </svg>

  <p class="contact contact--web">mquell@kplamail.com<br>www.kplahygiene.com</p>
  <p class="contact contact--address">041.12th floor.Hale Ridge<br>Road KPL</p>
  <p class="contact contact--phone">014 552 7830<br>014 552 7830</p>

  <svg class="band band--bottom" width="700" height="40" viewBox="0 0 700 40" aria-hidden="true">
    <rect width="700" height="40" fill="var(--blue)"/>
  </svg>
</section>

</body>
</html>
```